RTV CRAFTED

building services
decks
pergola
renovation
extensions
general building

Target Market(s)

middle to upper class

Industry/Entity Type

building

Contact Information for Business Card

my details 0427839152 pkharlow47@mailvane.net BLD574926

Font styles to use
Serif

Colors
00AB8E
00BBA5
67D7C9
C6EFE9
E9F9F6

Requirements
Must have
• logo on the front and details on the back
Nice to have
• sharp and clean lines

```html
<!DOCTYPE html>
<html lang="en">
<head>
<meta charset="utf-8">
<title>RTV Crafted — Business Card</title>
<link rel="stylesheet" href="https://fonts.googleapis.com/css2?family=Roboto:wght@300;400;500;700&display=swap">
<style>
  :root {
    --green: #41bb93;
    --teal: #68c9c8;
    --charcoal: #343a41;
    --paper: #ffffff;
    --ink: #2a2e33;
  }
  * { margin: 0; padding: 0; box-sizing: border-box; }
  html, body { width: 1200px; height: 1000px; overflow: hidden; background: var(--paper); }
  body { position: relative; font-family: "Roboto", Arial, sans-serif; color: var(--ink); }

  .card {
    position: absolute;
    left: 310px;
    width: 580px;
    height: 348px;
    background: var(--paper);
    box-shadow: 6px 8px 14px rgba(0,0,0,0.18);
    overflow: hidden;
  }
  .card--front { top: 112px; }
  .card--back { top: 540px; }
  .card__bands { position: absolute; left: 0; top: 0; width: 580px; height: 348px; }

  .brand {
    position: absolute;
    left: 0; right: 0; top: 150px;
    display: flex; justify-content: center; align-items: center; gap: 14px;
  }
  .brand__mark { width: 26px; height: 26px; background: var(--teal); }
  .brand__name {
    font-weight: 700; font-size: 46px; letter-spacing: 1px;
    color: var(--green);
  }

  .services-title {
    position: absolute; left: 40px; top: 38px;
    font-weight: 500; font-size: 20px; letter-spacing: 0.2px;
    padding-bottom: 3px;
    border-bottom: 3px solid var(--charcoal);
  }
  .services-title__lead { color: var(--green); }
  .services-title__tail { color: var(--teal); }

  .services {
    position: absolute; left: 41px; top: 110px;
    list-style: none;
  }
  .services__item {
    display: flex; align-items: center; gap: 9px;
    height: 26.7px;
    font-weight: 400; font-size: 16px; letter-spacing: 0.2px;
  }
  .services__bullet { width: 16px; height: 16px; background: var(--green); flex: none; }
  .services__bullet--teal { background: var(--teal); }

  .divider {
    position: absolute; left: 273px; top: 113px;
    width: 4px; height: 123px; background: var(--charcoal);
  }

  .contacts {
    position: absolute; right: 41px; top: 127px;
    list-style: none;
  }
  .contacts__item {
    display: flex; justify-content: flex-end; align-items: center; gap: 10px;
    height: 33.5px;
    font-weight: 400; font-size: 16px; letter-spacing: 0.1px;
  }
  .contacts__icon {
    width: 23px; height: 23px; background: var(--green);
    display: flex; align-items: center; justify-content: center; flex: none;
  }
</style>
</head>
<body>

  <section class="card card--front" aria-label="Card front">
    <svg class="card__bands" viewBox="0 0 580 348" aria-hidden="true">
      <polygon points="0,0 290,0 250,40 0,40" fill="var(--green)"/>
      <polygon points="0,40 215,40 200,55 0,55" fill="var(--teal)"/>
      <polygon points="300,0 580,0 580,40 260,40" fill="var(--charcoal)"/>
    </svg>
    <div class="brand">
      <span class="brand__mark"></span>
      <span class="brand__name">RTV CRAFTED</span>
    </div>
  </section>

  <section class="card card--back" aria-label="Card back">
    <svg class="card__bands" viewBox="0 0 580 348" aria-hidden="true">
      <polygon points="0,308 320,308 280,348 0,348" fill="var(--charcoal)"/>
      <polygon points="382,292 580,292 580,308 366,308" fill="var(--teal)"/>
      <polygon points="330,308 580,308 580,348 290,348" fill="var(--green)"/>
    </svg>

    <h2 class="services-title"><span class="services-title__lead">BUILDING</span> <span class="services-title__tail">SERVICES</span></h2>

    <ul class="services">
      <li class="services__item"><span class="services__bullet"></span>DECKS</li>
      <li class="services__item"><span class="services__bullet services__bullet--teal"></span>PERGOLA</li>
      <li class="services__item"><span class="services__bullet"></span>RENOVATION</li>
      <li class="services__item"><span class="services__bullet"></span>EXTENSIONS</li>
      <li class="services__item"><span class="services__bullet services__bullet--teal"></span>GENERAL BUILDING</li>
    </ul>

    <div class="divider"></div>

    <ul class="contacts">
      <li class="contacts__item">0427839152
        <span class="contacts__icon">
          <svg width="14" height="14" viewBox="0 0 14 14" aria-hidden="true">
            <path d="M1 4 Q7 0 13 4 L13 6 L10 6 L10 4.5 Q7 3.5 4 4.5 L4 6 L1 6 Z" fill="#fff"/>
            <rect x="2.5" y="7" width="9" height="6" rx="1" fill="#fff"/>
            <circle cx="7" cy="10" r="1.6" fill="var(--green)"/>
          </svg>
        </span>
      </li>
      <li class="contacts__item">pkharlow47@mailvane.net
        <span class="contacts__icon">
          <svg width="14" height="14" viewBox="0 0 14 14" aria-hidden="true">
            <path d="M2 2 L12 6 L8 7.5 L11.5 11 L10.5 12 L7 8.5 L5.5 12 Z" fill="#fff"/>
          </svg>
        </span>
      </li>
      <li class="contacts__item">BLD574926
        <span class="contacts__icon"></span>
      </li>
    </ul>
  </section>

</body>
</html>
```